Business card design needed for a security services business.

We provide a wide range of security services from guard personnel to electronic systems.

Industry/Entity Type

Security Industry

Contact Information for Business Card

Brent Holloway, Owner Office: 780.555.0148; Cell: 780.555.0193 Email: brent@korvanshieldgroup.example; Address 20417 163 St Edmonton, AB T5X 2K8

Colors
0054AA
0677BA
7BADD7
CADEEF
E8F1F8

Requirements
Nice to have
• On the back of the card I would like to possible list the services I provide: Guards Mobiles Live Video Surveillance Access Intrusion

```html
<!DOCTYPE html>
<html lang="en">
<head>
<meta charset="utf-8">
<title>Korvan Shield Group — Business Card</title>
<link href="https://fonts.googleapis.com/css2?family=Montserrat:wght@400;500;700&family=Oswald:wght@500&display=swap" rel="stylesheet">
<style>
  :root {
    --brand-blue: #0677BA;
    --deep-blue: #0054AA;
    --ink: #1f1f1f;
    --card-dark: #1c1c1d;
    --paper: #ffffff;
    --stage: #3a3a3a;
    --muted-line: #6b6b6b;
  }
  html, body {
    margin: 0;
    width: 1200px;
    height: 1200px;
    overflow: hidden;
    background: var(--stage);
  }
  .canvas {
    position: relative;
    width: 1200px;
    height: 1200px;
  }
  .card {
    position: absolute;
    left: 220px;
    width: 760px;
    height: 434px;
    border-radius: 28px;
    overflow: hidden;
    box-shadow: 0 18px 40px rgba(0,0,0,0.45);
  }
  /* ---------- Front ---------- */
  .card-front {
    top: 120px;
    background: var(--paper);
  }
  .identity {
    position: absolute;
    left: 58px;
    top: 150px;
    padding-left: 22px;
    border-left: 7px solid var(--brand-blue);
  }
  .person-name {
    font-family: 'Montserrat', sans-serif;
    font-weight: 700;
    font-size: 31px;
    letter-spacing: 0.5px;
    color: var(--brand-blue);
    margin: 0;
    line-height: 1;
  }
  .person-role {
    font-family: 'Montserrat', sans-serif;
    font-weight: 500;
    font-size: 19px;
    color: var(--ink);
    margin: 6px 0 0;
    line-height: 1;
  }
  .contact-list {
    position: absolute;
    left: 80px;
    top: 226px;
    margin: 0;
    padding: 0;
    list-style: none;
    font-family: 'Montserrat', sans-serif;
    font-size: 18px;
    color: var(--ink);
  }
  .contact-list li {
    display: flex;
    align-items: center;
    height: 25px;
  }
  .contact-icon {
    width: 18px;
    height: 18px;
    margin-right: 12px;
    fill: var(--brand-blue);
    flex: none;
  }
  .brand-front {
    position: absolute;
    right: 48px;
    top: 78px;
    display: flex;
    align-items: center;
    gap: 12px;
  }
  .brand-mark {
    width: 22px;
    height: 22px;
    background: var(--brand-blue);
    flex: none;
  }
  .brand-name {
    font-family: 'Montserrat', sans-serif;
    font-weight: 700;
    font-size: 30px;
    letter-spacing: 1px;
    color: var(--brand-blue);
    margin: 0;
    line-height: 1.05;
  }
  .service-band {
    position: absolute;
    left: 0;
    right: 0;
    top: 338px;
    height: 44px;
    background: var(--brand-blue);
    display: flex;
    align-items: center;
    justify-content: flex-end;
    padding-right: 78px;
    box-sizing: border-box;
    gap: 22px;
    font-family: 'Oswald', sans-serif;
    font-weight: 500;
    font-size: 19px;
    color: var(--paper);
    text-transform: uppercase;
  }
  .service-band span::before {
    content: "•";
    margin-right: 8px;
  }
  /* ---------- Back ---------- */
  .card-back {
    top: 646px;
    background: linear-gradient(110deg, #181818 0%, #232324 45%, #2c2c2d 55%, #1a1a1a 100%);
  }
  .brand-back {
    position: absolute;
    left: 0;
    right: 0;
    top: 140px;
    text-align: center;
  }
  .brand-back .brand-name {
    font-size: 50px;
    letter-spacing: 2px;
  }
  .brand-rule {
    display: block;
    margin: 18px auto 0;
    width: 520px;
    height: 3px;
    background: var(--paper);
  }
  .accent-bar {
    position: absolute;
    right: 0;
    bottom: 52px;
    width: 460px;
    height: 22px;
    background: var(--brand-blue);
  }
</style>
</head>
<body>
<main class="canvas">

  <section class="card card-front" aria-label="Business card front">
    <div class="brand-front">
      <span class="brand-mark" aria-hidden="true"></span>
      <p class="brand-name">KORVAN SHIELD<br>GROUP</p>
    </div>

    <div class="identity">
      <h1 class="person-name">BRENT HOLLOWAY</h1>
      <p class="person-role">OWNER</p>
    </div>

    <ul class="contact-list">
      <li>
        <svg class="contact-icon" viewBox="0 0 24 24" aria-hidden="true"><path d="M6.6 10.8a15.1 15.1 0 0 0 6.6 6.6l2.2-2.2c.3-.3.7-.4 1-.2 1.1.4 2.3.6 3.6.6.6 0 1 .4 1 1V20c0 .6-.4 1-1 1A17 17 0 0 1 3 4c0-.6.4-1 1-1h3.5c.6 0 1 .4 1 1 0 1.3.2 2.5.6 3.6.1.3 0 .7-.2 1z"/></svg>
        780.555.0148
      </li>
      <li>
        <svg class="contact-icon" viewBox="0 0 24 24" aria-hidden="true"><path d="M7 1h10a2 2 0 0 1 2 2v18a2 2 0 0 1-2 2H7a2 2 0 0 1-2-2V3a2 2 0 0 1 2-2zm0 3v14h10V4zm5 15.5a1.2 1.2 0 1 0 0 2.4 1.2 1.2 0 0 0 0-2.4z"/></svg>
        780.555.0193
      </li>
      <li>
        <svg class="contact-icon" viewBox="0 0 24 24" aria-hidden="true"><path d="M2 5h20v14H2zm2 2v.4l8 5.2 8-5.2V7zm0 2.8V17h16V9.8l-8 5.2z"/></svg>
        brent@korvanshieldgroup.example
      </li>
      <li>
        <svg class="contact-icon" viewBox="0 0 24 24" aria-hidden="true"><path d="M12 2a7 7 0 0 0-7 7c0 5.2 7 13 7 13s7-7.8 7-13a7 7 0 0 0-7-7zm0 9.5a2.5 2.5 0 1 1 0-5 2.5 2.5 0 0 1 0 5z"/></svg>
        20417 163 St Edmonton, AB T5X 2K8
      </li>
    </ul>

    <div class="service-band">
      <span>Guards Mobiles</span>
      <span>Live Video Surveillance</span>
      <span>Access Intrusion</span>
    </div>
  </section>

  <section class="card card-back" aria-label="Business card back">
    <div class="brand-back">
      <p class="brand-name">KORVAN SHIELD<br>GROUP</p>
      <span class="brand-rule" aria-hidden="true"></span>
    </div>
    <span class="accent-bar" aria-hidden="true"></span>
  </section>

</main>
</body>
</html>
```